Design a styled business card for an intimacy and attachment psychologist

I am a Psychologist providing online therapy to patients across the United States. My work is interpersonal and emotion-focused, with an emphasis on the client-therapist relationship. My primary areas of work are very personal, including sexuality and gender, abuse and trauma, and grief and loss. My target audience will be adults of all ages 18+.
My business card should convey a warm and inviting feeling of professionalism that is also casual and comfortable.
The front should be fairly simple and professional, consisting of:
- My name, Dr. Rosalind Petrakis
- My title, Licensed Psycholigist
- My logo
On either the front or the back, my contact information should be listed:
- ros@drrospetrakis.example
- 555.014.7788
- drrospetrakis.example
On the rear, I would like a description of the areas that I specialize in. This can be formatted in any way that appears stylistically interesting.
Individual and Couples
Relationships and Infidelity
Sexual Health & Aging
Gender Identity & Sexual Orientation
Abuse and Trauma
Sexual Compulsivity & Addiction
Sexual Dysfunction
Target Market(s)
My target audience will be adults of all ages 18+.
Industry/Entity Type
Psychology
Contact Information for Business Card
The front should be fairly simple and professional, consisting of: - My name, Dr. Rosalind Petrakis - My title, Licensed Psycholigist - My logo On either the front or the back, my contact information should be listed: - ros@drrospetrakis.example - 555.014.7788 - drrospetrakis.example On the rear, I would like a description of the areas that I specialize in. This can be formatted in any way that appears stylistically interesting. Individual and Couples Relationships and Infidelity Sexual Health & Aging Gender Identity & Sexual Orientation Abuse and Trauma Sexual Compulsivity & Addiction Sexual Dysfunction
- Follow brand guide

```html
<!DOCTYPE html>
<html lang="en">
<head>
<meta charset="utf-8">
<title>Dr. Rosalind Petrakis — Business Card</title>
<link rel="stylesheet" href="https://fonts.googleapis.com/css2?family=Cinzel:wght@500&family=Lato:wght@400;700;900&display=swap">
<style>
  :root {
    --bg: #e7e3de;
    --card: #ffffff;
    --navy: #27224a;
    --teal: #4dd4b3;
    --mint: #c9efe6;
    --purple: #a463c9;
    --red: #ef4149;
    --orange: #fbae22;
    --white: #ffffff;
  }
  * { box-sizing: border-box; margin: 0; padding: 0; }
  html, body { width: 1200px; height: 977px; overflow: hidden; }
  body {
    background: var(--bg);
    font-family: "Lato", sans-serif;
    position: relative;
  }
  .card {
    position: absolute;
    left: 250px;
    width: 700px;
    height: 400px;
    background: var(--card);
    border-radius: 22px;
    overflow: hidden;
    box-shadow: 0 6px 18px rgba(0,0,0,0.12);
  }
  .card--front { top: 58px; }
  .card--back { top: 518px; }

  /* Front */
  .front-mark {
    position: absolute;
    inset: 0;
    display: flex;
    align-items: center;
    justify-content: center;
    gap: 34px;
  }
  .mark-dot {
    width: 130px; height: 130px;
    border-radius: 50%;
    background: var(--teal);
    flex: none;
  }
  .front-name {
    font-family: "Cinzel", serif;
    font-weight: 500;
    color: var(--navy);
    font-size: 46px;
    line-height: 1.1;
  }

  /* Back */
  .back-art { position: absolute; inset: 0; }
  .back-info {
    position: absolute;
    left: 48px;
    top: 46px;
    color: var(--white);
  }
  .back-name {
    color: var(--teal);
    font-weight: 900;
    font-size: 29px;
    text-transform: uppercase;
    letter-spacing: 0.2px;
    line-height: 1.15;
  }
  .back-title {
    font-size: 19px;
    font-weight: 700;
    margin-top: 2px;
  }
  .contact-list, .specialty-list { list-style: none; }
  .contact-list { margin-top: 14px; }
  .contact-list li {
    display: flex; align-items: center; gap: 10px;
    font-size: 16px; line-height: 23px;
  }
  .contact-list svg { width: 14px; height: 14px; fill: var(--teal); flex: none; }
  .specialty-list { margin-top: 16px; }
  .specialty-list li {
    display: flex; align-items: center; gap: 12px;
    font-size: 15.5px; line-height: 21px;
  }
  .specialty-list li::before {
    content: "";
    width: 8px; height: 8px; border-radius: 50%;
    background: var(--teal); flex: none;
  }
  .back-mark {
    position: absolute;
    right: 48px;
    top: 50%;
    transform: translateY(-50%);
    width: 150px;
    display: flex;
    flex-direction: column;
    align-items: center;
    gap: 16px;
  }
  .back-mark .mark-dot { width: 120px; height: 120px; }
  .back-mark-name {
    font-family: "Cinzel", serif;
    font-weight: 500;
    color: var(--navy);
    font-size: 17px;
    text-align: center;
    line-height: 1.2;
  }
</style>
</head>
<body>
  <section class="card card--front">
    <div class="front-mark">
      <span class="mark-dot"></span>
      <p class="front-name">Dr. Rosalind<br>Petrakis</p>
    </div>
  </section>

  <section class="card card--back">
    <svg class="back-art" viewBox="0 0 700 400" preserveAspectRatio="none" aria-hidden="true">
      <path d="M0 0 H420 C360 120 540 250 520 400 H0 Z" fill="var(--navy)"/>
      <path d="M420 0 C360 120 540 250 520 400" fill="none" stroke="var(--purple)" stroke-width="7"/>
      <path d="M432 0 C378 120 556 250 534 400" fill="none" stroke="var(--red)" stroke-width="6"/>
      <path d="M446 0 C398 110 570 240 552 400" fill="none" stroke="var(--orange)" stroke-width="5"/>
    </svg>

    <div class="back-info">
      <h1 class="back-name">Dr. Rosalind Petrakis</h1>
      <p class="back-title">Licensed Psycholigist</p>
      <ul class="contact-list">
        <li><svg viewBox="0 0 24 24"><path d="M6.6 10.8a15.1 15.1 0 0 0 6.6 6.6l2.2-2.2c.3-.3.7-.4 1-.2 1.1.4 2.3.6 3.6.6.6 0 1 .4 1 1V20c0 .6-.4 1-1 1A17 17 0 0 1 3 4c0-.6.4-1 1-1h3.5c.6 0 1 .4 1 1 0 1.3.2 2.5.6 3.6.1.3 0 .7-.2 1z"/></svg>555.014.7788</li>
        <li><svg viewBox="0 0 24 24"><path d="M2 5h20v14H2z M2 5l10 8 10-8" /></svg>ros@drrospetrakis.example</li>
        <li><svg viewBox="0 0 24 24"><path d="M12 2a10 10 0 1 0 0 20 10 10 0 0 0 0-20zm0 2c.9 1.2 1.7 3.1 2 5h-4c.3-1.9 1.1-3.8 2-5zM4.3 13a8 8 0 0 1 0-2h3.8a16 16 0 0 0 0 2zm.8 2h3.2c.3 1.4.8 2.7 1.4 3.8A8 8 0 0 1 5.1 15zm3.2-6H5.1a8 8 0 0 1 4.6-3.8C9.1 6.3 8.6 7.6 8.3 9zM12 20c-.9-1.2-1.7-3.1-2-5h4c-.3 1.9-1.1 3.8-2 5zm2.2-7h-4.4a14 14 0 0 1 0-2h4.4a14 14 0 0 1 0 2zm.1 5.8c.6-1.1 1.1-2.4 1.4-3.8h3.2a8 8 0 0 1-4.6 3.8zm1.6-5.8a16 16 0 0 0 0-2h3.8a8 8 0 0 1 0 2zm-.2-4c-.3-1.4-.8-2.7-1.4-3.8A8 8 0 0 1 18.9 9z"/></svg>drrospetrakis.example</li>
      </ul>
      <ul class="specialty-list">
        <li>Individual &amp; Couples</li>
        <li>Relationships &amp; Infidelity</li>
        <li>Sexual Health &amp; Aging</li>
        <li>Gender Identity &amp; Sexual Orientation</li>
        <li>Abuse &amp; Trauma</li>
        <li>Sexual Compulsivity &amp; Addiction</li>
        <li>Sexual Dysfunction</li>
      </ul>
    </div>

    <div class="back-mark">
      <span class="mark-dot"></span>
      <p class="back-mark-name">Dr. Rosalind Petrakis</p>
    </div>
  </section>
</body>
</html>
```